依頼概要
■依頼目的 / 概要
電子書籍Lumora本を出版いたしますので、
表紙デザイン作成をお願いいたします。

■納品物
下記での納品をお願い致します。

JPEG形式 及び PSD形式
横1600ピクセル x 縦2560ピクセル

■本の内容

<本のタイトル>
ソラノワ-SKY RING-
老職人に学んだ
はじめての家庭づくりのガイドブック

<著者名>
浅井徹郎

■デザイン要望
・本のタイトル / 著者名の反映をお願いします

デザインイメージ

・基本的に青系の色合い

・シンプルな背景にタイトル等のコピーを記載

・ターゲットは子どもを持つご両親。

・お子様の子育てに関する細かいノウハウというよりも、
最も要となる考え方をお伝えしています。

・信頼感のあるデザインを希望します。

<表現したいイメージなど>
・信頼感

<表現したくないイメージ>
・安っぽい
・嘘くさい
・大衆的

<利用画像について>
画像素材を使用される場合には、
商用利用可の素材をお願いします。

■その他
デザインを考えるのに必要な情報が他にございましたら、
お答えしますので、遠慮なくご連絡ください。

*添付ファイルは、過去電子書籍の表紙デザインです。
*ジャンルが異なりますので、デザインテイストは今回とは、異なります。
*あくまでも、表紙に出てくる要素(タイトルや著者名など)の参考としてご利用ください。

意図をしっかりとご理解いただき、
目につく素晴らしいデザインに仕上げていただきました。
ありがとうございます。

この度は応募いただきありがとうございました。
近いうちにまた同じく、表紙のデザインをお願いする予定です。
またご参加くださいませ。

```html
<!DOCTYPE html>
<html lang="ja">
<head>
<meta charset="utf-8">
<title>ソラノワ -SKY RING- 表紙</title>
<link rel="stylesheet" href="https://fonts.googleapis.com/css2?family=Noto+Sans+JP:wght@700;900&family=Roboto:wght@700;900&display=swap">
<style>
  :root {
    --navy: #1c2a8c;
    --title-blue: #1f2f94;
    --white: #ffffff;
    --sky-top: #a9b7cc;
    --sky-mid: #c3a9b4;
    --glow: #f1c27a;
    --glow-deep: #e49a52;
    --ground: #6a5a66;
  }
  html, body {
    margin: 0;
    padding: 0;
    width: 750px;
    height: 1200px;
    overflow: hidden;
    background: #ffffff;
  }
  .cover {
    position: relative;
    width: 750px;
    height: 1200px;
    overflow: hidden;
    font-family: "Noto Sans JP", sans-serif;
  }
  .cover-backdrop {
    position: absolute;
    inset: 0;
    background:
      radial-gradient(ellipse 70% 45% at 30% 88%, var(--glow) 0%, rgba(241,194,122,0.55) 40%, rgba(241,194,122,0) 75%),
      linear-gradient(180deg, var(--sky-top) 0%, #b5b3c6 35%, var(--sky-mid) 58%, var(--glow-deep) 82%, var(--ground) 100%);
  }
  .series-title {
    position: absolute;
    left: 18px;
    top: 8px;
    margin: 0;
    font-weight: 900;
    font-size: 104px;
    line-height: 1.3;
    letter-spacing: 2px;
    color: var(--title-blue);
  }
  .title-rule {
    position: absolute;
    left: 18px;
    top: 146px;
    width: 530px;
    height: 3px;
    background: var(--navy);
  }
  .subtitle {
    position: absolute;
    left: 222px;
    top: 166px;
    margin: 0;
    font-weight: 900;
    font-size: 46px;
    line-height: 70px;
    color: var(--title-blue);
  }
  .subtitle span { display: block; }
  .author-label {
    position: absolute;
    right: 218px;
    top: 530px;
    font-weight: 700;
    font-size: 28px;
    letter-spacing: 4px;
    color: var(--navy);
  }
  .author-name {
    position: absolute;
    right: 218px;
    top: 566px;
    margin: 0;
    font-weight: 900;
    font-size: 60px;
    line-height: 1.1;
    letter-spacing: 2px;
    color: var(--navy);
  }
  .side-band {
    position: absolute;
    left: 555px;
    top: 12px;
    width: 176px;
    height: 1176px;
    background: var(--navy);
    box-sizing: border-box;
    border: 6px solid var(--navy);
    outline: 4px solid var(--white);
    outline-offset: -14px;
    display: flex;
    align-items: center;
    justify-content: center;
  }
  .side-band-text {
    writing-mode: vertical-rl;
    text-orientation: sideways;
    font-family: "Roboto", sans-serif;
    font-weight: 900;
    font-size: 150px;
    line-height: 1;
    letter-spacing: 4px;
    color: var(--white);
    white-space: nowrap;
  }
</style>
</head>
<body>
  <main class="cover">
    <div class="cover-backdrop" role="img" aria-label="夕日の光を背に拳を掲げる人物のシルエット写真"></div>

    <h1 class="series-title">ソラノワ</h1>
    <div class="title-rule"></div>

    <p class="subtitle">
      <span>老職人に学んだ</span>
      <span>はじめての</span>
      <span>家庭づくりの</span>
      <span>ガイドブック</span>
    </p>

    <div class="author-label">著者</div>
    <p class="author-name">浅井 徹郎</p>

    <aside class="side-band">
      <span class="side-band-text">-SKY RING-</span>
    </aside>
  </main>
</body>
</html>
```